New Poster Design for Film Festival

Hi! We need a poster design for our student film festival and the Harlow Ridge University. We screen over 300 short films over a 3 days in May. Our committee wants a look feel similar to the image we attached below.

Target Market(s)

Students and general audience.

Industry/Entity Type

Festival

Colors
3377b5
85abd2
34b8a4
f68e4e

Requirements
Must have
• Otters Film Festival
17th Annual
May 2-3-4 2014
Ned Varrow Cinema
Free Admission
Department of Screen and Digital Narrative

Poster size 36" (high) x 24" (wide)
Harlow Ridge University
www.ottersfilmfest.example
Nice to have
• Bold lettering
Should not have
• Flamingos - hate them :)

```html
<!DOCTYPE html>
<html lang="en">
<head>
<meta charset="utf-8">
<title>17th Annual Otters Film Festival</title>
<link rel="stylesheet" href="https://fonts.googleapis.com/css2?family=Bebas+Neue&family=Lobster+Two:wght@700&display=swap">
<style>
  :root {
    --paper: #ffffff;
    --festival-blue: #3377b5;
    --sky-blue: #85abd2;
    --teal: #34b8a4;
    --orange: #f68e4e;
    --ink: #1e1e1e;
    --rule: #2b2b2b;
  }
  html, body {
    margin: 0;
    padding: 0;
    width: 807px;
    height: 1200px;
    overflow: hidden;
    background: var(--paper);
  }
  .poster {
    position: relative;
    width: 807px;
    height: 1200px;
    background: var(--paper);
    overflow: hidden;
  }
  .camera-collage {
    position: absolute;
    left: 9px;
    top: 9px;
    width: 789px;
    height: 966px;
    background:
      radial-gradient(ellipse 14% 11% at 52% 46%, rgba(246,142,78,0.95) 0, rgba(246,142,78,0.6) 60%, rgba(246,142,78,0) 100%),
      radial-gradient(ellipse 30% 22% at 50% 45%, rgba(30,30,30,0.35) 0, rgba(30,30,30,0.15) 70%, rgba(30,30,30,0) 100%),
      radial-gradient(ellipse 22% 14% at 12% 12%, rgba(52,184,164,0.85) 0, rgba(52,184,164,0) 100%),
      radial-gradient(ellipse 20% 12% at 60% 4%, rgba(246,142,78,0.7) 0, rgba(246,142,78,0) 100%),
      radial-gradient(ellipse 18% 14% at 92% 20%, rgba(52,184,164,0.7) 0, rgba(52,184,164,0) 100%),
      radial-gradient(ellipse 16% 12% at 6% 40%, rgba(246,142,78,0.7) 0, rgba(246,142,78,0) 100%),
      radial-gradient(ellipse 20% 14% at 14% 84%, rgba(51,119,181,0.9) 0, rgba(51,119,181,0) 100%),
      radial-gradient(ellipse 16% 10% at 36% 74%, rgba(246,142,78,0.6) 0, rgba(246,142,78,0) 100%),
      radial-gradient(ellipse 18% 12% at 62% 92%, rgba(51,119,181,0.7) 0, rgba(51,119,181,0) 100%),
      radial-gradient(ellipse 18% 12% at 92% 94%, rgba(246,142,78,0.8) 0, rgba(246,142,78,0) 100%),
      radial-gradient(ellipse 16% 12% at 90% 60%, rgba(52,184,164,0.6) 0, rgba(52,184,164,0) 100%),
      radial-gradient(ellipse 18% 12% at 30% 28%, rgba(51,119,181,0.6) 0, rgba(51,119,181,0) 100%),
      radial-gradient(ellipse 16% 12% at 45% 88%, rgba(52,184,164,0.6) 0, rgba(52,184,164,0) 100%),
      linear-gradient(160deg, #cfdff0 0%, #f4f8fc 40%, #e6eef7 60%, #c6d8eb 100%);
  }
  .collage-rule {
    position: absolute;
    left: 9px;
    top: 975px;
    width: 789px;
    height: 1px;
    background: var(--rule);
  }
  .festival-title {
    position: absolute;
    left: 0;
    top: 983px;
    width: 807px;
    margin: 0;
    text-align: center;
    font-family: "Bebas Neue", "Oswald", sans-serif;
    font-weight: 400;
    font-size: 60px;
    line-height: 60px;
    letter-spacing: 0;
    color: var(--orange);
  }
  .festival-title span {
    display: inline-block;
    transform: scaleX(0.92);
  }
  .festival-details {
    position: absolute;
    left: 0;
    top: 1056px;
    width: 807px;
    margin: 0;
    padding: 0;
    list-style: none;
    text-align: center;
    font-family: "Lobster Two", cursive;
    font-weight: 700;
    font-size: 21px;
    line-height: 21px;
    letter-spacing: 0.6px;
    color: var(--festival-blue);
  }
</style>
</head>
<body>
  <main class="poster">
    <div class="camera-collage" role="img" aria-label="Collage of vintage and modern film and video cameras in black, blue, teal and orange overlapping silhouettes"></div>
    <div class="collage-rule"></div>
    <h1 class="festival-title"><span>17th Annual Otters Film Festival</span></h1>
    <ul class="festival-details">
      <li>May 2nd, 3rd, and 4th 2014</li>
      <li>Ned Varrow cinema</li>
      <li>Free Admission</li>
      <li>department of screen and digital narrative</li>
      <li>Harlow Ridge University</li>
      <li>www.ottersfilmfest.example</li>
    </ul>
  </main>
</body>
</html>
```